Business Card design for a skin clinic

i would like a business card design for our skin clinic.
our logo colors are Blue and Grey and Bule /white.
we are searching for a minimalistic design yet very elegant,dynamic and professional which can reflect a professional medical skin care clinic( not a beauty salon).
THE DESGIN IS NOT FOR A PERSON IT WILL BE USED IN THE CLINIC FOR CLIENTS SO THERE SHOULD BE NO NAME OF A PERSON ONLY THE CLINIC NAME AND THE CONTACT INFO

Target Market(s)
young and old womens
Industry/Entity Type
Business
Contact Information for Business Card
we have 2 address and both should be on the card.
address A: Lindenhoflaan 214B, 3041KP Rotterdam, Tel 010 483 21 95
address B: Zonnewijzerstraat 238, 1062RT Amsterdam Tel 020 571 3829
website www.huidpuntzorg.nu, email info@huidpuntzorg.nu
Look and feel
Each slider illustrates characteristics of the customer's brand and the style your logo design should communicate.

```html
<!DOCTYPE html>
<html lang="nl">
<head>
<meta charset="utf-8">
<title>Huidpuntzorg – business card</title>
<link rel="stylesheet" href="https://fonts.googleapis.com/css2?family=Questrial&family=Open+Sans:wght@400;600&display=swap">
<style>
  :root {
    --backdrop: #6b6b6b;
    --brand-blue: #2f86c8;
    --card-blue: #3a88c9;
    --band-blue-a: #3f86cc;
    --band-blue-b: #2995d1;
    --band-blue-c: #4b7ec6;
    --grey-text: #555a60;
    --tagline-grey: #8a8f94;
    --white: #ffffff;
  }
  * { margin: 0; padding: 0; box-sizing: border-box; }
  html, body { width: 1200px; height: 900px; overflow: hidden; }
  body {
    background: radial-gradient(ellipse at 50% 40%, #707070 0%, var(--backdrop) 70%);
    position: relative;
    font-family: "Open Sans", Arial, sans-serif;
  }
  .card {
    position: absolute;
    top: 306px;
    width: 440px;
    height: 271px;
    border-radius: 12px;
    overflow: hidden;
    box-shadow: 0 1px 3px rgba(0,0,0,.25);
  }
  .card-front { left: 149px; background: var(--white); }
  .card-back { left: 608px; background: var(--card-blue); }

  /* front: header */
  .front-header { position: absolute; left: 0; top: 0; width: 100%; height: 122px; }
  .brand-name {
    position: absolute; left: 23px; top: 40px;
    font-family: "Questrial", Arial, sans-serif;
    font-size: 25px; letter-spacing: 1.5px;
    color: var(--brand-blue);
  }
  .brand-tagline {
    position: absolute; left: 45px; top: 72px;
    font-family: "Questrial", Arial, sans-serif;
    font-size: 11px; letter-spacing: 1.2px;
    color: var(--tagline-grey);
  }

  /* front: contact band */
  .front-divider {
    position: absolute; left: 0; top: 122px; width: 100%; height: 4px;
    background: linear-gradient(#5a5a5a, #8a8a8a);
  }
  .contact-band {
    position: absolute; left: 0; top: 126px; width: 100%; height: 145px;
    background: linear-gradient(120deg, var(--band-blue-a) 0%, var(--band-blue-b) 45%, var(--band-blue-c) 100%);
    color: var(--white);
    font-size: 12px;
  }
  .contact-list { position: absolute; left: 23px; top: 27px; list-style: none; }
  .contact-list li, .address-phone { display: flex; align-items: center; height: 16px; }
  .icon { width: 9px; height: 9px; margin-right: 5px; fill: var(--white); flex: none; }
  .address { position: absolute; top: 76px; line-height: 16px; }
  .address-rotterdam { left: 23px; }
  .address-amsterdam { left: 215px; }
</style>
</head>
<body>

<section class="card card-front">
  <header class="front-header">
    <div class="brand-name">HUIDPUNTZORG</div>
    <div class="brand-tagline">next generation skin care</div>
  </header>
  <div class="front-divider"></div>
  <div class="contact-band">
    <ul class="contact-list">
      <li>
        <svg class="icon" viewBox="0 0 10 10"><path d="M0.5 2h9v6h-9z"/><path d="M1 2.5l4 3 4-3" stroke="#3a8acb" stroke-width="0.8" fill="none"/></svg>
        info@huidpuntzorg.nu
      </li>
      <li>
        <svg class="icon" viewBox="0 0 10 10"><circle cx="5" cy="5" r="4.5"/></svg>
        www.huidpuntzorg.nu
      </li>
    </ul>
    <div class="address address-rotterdam">
      <div>Lindenhoflaan 214B,</div>
      <div>3041KP Rotterdam</div>
      <div class="address-phone">
        <svg class="icon" viewBox="0 0 10 10"><path d="M2 0.5l1.6 2.2-0.9 1c0.6 1.3 1.3 2 2.6 2.6l1-0.9 2.2 1.6-0.9 1.9C4.4 8.7 1.3 5.6 0.1 1.4z"/></svg>
        010 483 21 95
      </div>
    </div>
    <div class="address address-amsterdam">
      <div>Zonnewijzerstraat 238,</div>
      <div>1062RT Amsterdam</div>
      <div class="address-phone">
        <svg class="icon" viewBox="0 0 10 10"><path d="M2 0.5l1.6 2.2-0.9 1c0.6 1.3 1.3 2 2.6 2.6l1-0.9 2.2 1.6-0.9 1.9C4.4 8.7 1.3 5.6 0.1 1.4z"/></svg>
        020 571 3829
      </div>
    </div>
  </div>
</section>

<section class="card card-back">
  <div class="back-pattern" role="img" aria-label="Faint repeating brand monogram pattern in tone-on-tone blue" style="position:absolute;inset:0;background:linear-gradient(135deg,#3786c7,#3b8aca);"></div>
  <div style="position:absolute;left:50%;top:88px;transform:translateX(-50%);width:14px;height:14px;border-radius:50%;background:var(--white);" class="back-mark"></div>
  <div class="back-name" style="position:absolute;left:0;width:100%;top:145px;text-align:center;font-family:'Questrial',Arial,sans-serif;font-size:29px;letter-spacing:2px;color:var(--white);">HUIDPUNTZORG</div>
  <div class="back-tagline" style="position:absolute;left:0;width:100%;top:186px;text-align:center;font-family:'Questrial',Arial,sans-serif;font-size:13px;letter-spacing:1.5px;color:var(--white);">next generation skin care</div>
  <div class="back-web" style="position:absolute;left:0;width:100%;top:228px;text-align:center;font-size:12px;color:var(--white);">www.huidpuntzorg.nu</div>
</section>

</body>
</html>
```